Stationery design for online marketing company
Vumor
Stationery design for online marketing company - Marketing
Creative Brief
Use specific fonts
Feel free
Bright & Fun-filled
Ruth K. Dallimore
Project Director
Vumor Online Market Ltd 17 Marlowe Ridge Street Pelvine District Abuja, Nigeria
ruth@vumor.com
www.vumor.com
RC5073316
tepluwin tepluwin
Dear All, Please, you may want to include the letterhead design, email signature design etc

```html
<!DOCTYPE html>
<html lang="en">
<head>
<meta charset="utf-8">
<title>Vumor Business Card</title>
<link href="https://fonts.googleapis.com/css2?family=Montserrat:wght@400;500;600;700;800&display=swap" rel="stylesheet">
<style>
  :root {
    --stage: #e6e6e6;
    --card-dark: #1f1f21;
    --card-light: #ffffff;
    --brand-red: #e8302a;
    --brand-orange: #f36f21;
    --brand-amber: #f7b21c;
    --brand-yellow: #f6e61a;
    --brand-blue: #8aa2cf;
    --ink: #2b2b2b;
    --white: #ffffff;
  }
  * { margin: 0; padding: 0; box-sizing: border-box; }
  html, body { width: 1200px; height: 790px; overflow: hidden; }
  body {
    background: var(--stage);
    font-family: "Montserrat", Arial, sans-serif;
    position: relative;
  }
  .card {
    position: absolute;
    top: 233px;
    width: 470px;
    height: 273px;
    border-radius: 14px;
    overflow: hidden;
    box-shadow: 0 3px 10px rgba(0,0,0,0.18);
  }
  .card-front { left: 103px; background: var(--card-dark); }
  .card-back {
    left: 600px;
    background: linear-gradient(90deg, var(--brand-red) 0%, var(--brand-orange) 25%, var(--brand-amber) 48%, var(--brand-yellow) 66%, #e4e04c 80%, var(--brand-blue) 100%);
  }

  .accent-area {
    position: absolute;
    left: 222px;
    top: 0;
    width: 56px;
    height: 273px;
    background: linear-gradient(90deg, var(--brand-yellow), var(--brand-amber) 50%, var(--brand-red));
    opacity: 0.85;
  }
  .info-panel {
    position: absolute;
    left: 278px;
    top: 0;
    right: 0;
    bottom: 0;
    background: var(--card-light);
  }

  .brand { position: absolute; display: flex; align-items: center; gap: 8px; }
  .brand-dot { border-radius: 50%; flex: none; }
  .brand-name { font-weight: 800; letter-spacing: 0.5px; line-height: 1; }
  .tagline { position: absolute; line-height: 1; }

  .card-front .brand { left: 24px; top: 30px; }
  .card-front .brand-dot { width: 14px; height: 14px; background: var(--brand-orange); }
  .card-front .brand-name { font-size: 32px; color: var(--brand-orange); }
  .card-front .tagline { left: 26px; top: 70px; font-size: 9px; color: var(--white); letter-spacing: 0.3px; }

  .holder { position: absolute; left: 24px; top: 138px; }
  .holder-name { font-size: 16px; font-weight: 700; color: var(--brand-orange); }
  .holder-title { font-size: 9px; color: var(--white); margin-top: 3px; }
  .holder-contact { position: absolute; left: 24px; top: 184px; font-size: 9.5px; color: var(--white); }
  .holder-contact li { list-style: none; display: flex; align-items: center; gap: 7px; margin-bottom: 5px; }
  .icon { width: 10px; height: 10px; flex: none; }

  .company { position: absolute; right: 26px; top: 58px; text-align: right; color: var(--ink); font-size: 9px; line-height: 1.45; }
  .company-name { font-weight: 700; font-size: 10px; }
  .company-lines { margin-top: 14px; }
  .company-lines li { list-style: none; display: flex; justify-content: flex-end; align-items: center; gap: 6px; }
  .company-lines .icon { fill: var(--ink); }
  .license { margin-top: 10px; }

  .card-back .brand { left: 100px; top: 92px; gap: 14px; }
  .card-back .brand-dot { width: 36px; height: 36px; background: var(--white); }
  .card-back .brand-name { font-size: 74px; color: var(--white); }
  .card-back .tagline { left: 128px; top: 176px; font-size: 19px; font-weight: 600; color: var(--white); }
</style>
</head>
<body>

<section class="card card-front">
  <div class="accent-area" role="img" aria-label="Colourful decorative swoosh divider"></div>
  <div class="info-panel"></div>

  <div class="brand">
    <span class="brand-dot"></span>
    <span class="brand-name">Vumor</span>
  </div>
  <p class="tagline">buy smart, sell fast!</p>

  <div class="holder">
    <p class="holder-name">Ruth K. Dallimore</p>
    <p class="holder-title">Project Director</p>
  </div>
  <ul class="holder-contact">
    <li>
      <svg class="icon" viewBox="0 0 10 10"><path d="M2 0.5 L4 2.5 L3 3.8 C3.8 5.3 4.7 6.2 6.2 7 L7.5 6 L9.5 8 L8 9.5 C4 9 1 6 0.5 2 Z" fill="var(--brand-orange)"/></svg>
      0803 555 0142
    </li>
    <li>
      <svg class="icon" viewBox="0 0 10 10"><rect x="0.5" y="2" width="9" height="6.5" fill="var(--brand-orange)"/><path d="M0.5 2 L5 5.5 L9.5 2" fill="none" stroke="var(--card-dark)" stroke-width="0.9"/></svg>
      ruth@vumor.com
    </li>
  </ul>

  <div class="company">
    <p class="company-name">Vumor Online Market Ltd</p>
    <p>17 Marlowe Ridge Street</p>
    <p>Pelvine District, Abuja, Nigeria</p>
    <ul class="company-lines">
      <li>(T) 0800 555 0190 <svg class="icon" viewBox="0 0 10 10"><path d="M2 0.5 L4 2.5 L3 3.8 C3.8 5.3 4.7 6.2 6.2 7 L7.5 6 L9.5 8 L8 9.5 C4 9 1 6 0.5 2 Z"/></svg></li>
      <li>0805 555 0177 <svg class="icon" viewBox="0 0 10 10"><path d="M2 0.5 L4 2.5 L3 3.8 C3.8 5.3 4.7 6.2 6.2 7 L7.5 6 L9.5 8 L8 9.5 C4 9 1 6 0.5 2 Z"/></svg></li>
      <li>340 555 0163 <svg class="icon" viewBox="0 0 10 10"><path d="M2 0.5 L4 2.5 L3 3.8 C3.8 5.3 4.7 6.2 6.2 7 L7.5 6 L9.5 8 L8 9.5 C4 9 1 6 0.5 2 Z"/></svg></li>
      <li>www.vumor.com <svg class="icon" viewBox="0 0 10 10"><circle cx="5" cy="5" r="4.3" fill="none" stroke="var(--ink)" stroke-width="1"/><path d="M0.7 5 H9.3 M5 0.7 C2.5 3 2.5 7 5 9.3 M5 0.7 C7.5 3 7.5 7 5 9.3" fill="none" stroke="var(--ink)" stroke-width="0.8"/></svg></li>
    </ul>
    <div class="license">
      <p>License No., if any</p>
      <p>RC5073316</p>
    </div>
  </div>
</section>

<section class="card card-back">
  <div class="brand">
    <span class="brand-dot"></span>
    <span class="brand-name">Vumor</span>
  </div>
  <p class="tagline">buy smart, sell fast!</p>
</section>

</body>
</html>
```